National Virtual CPA Firm needs post card design

Virtual CPA firm called "BRELLVO" needs a 5.5” x 8.5” post card designed to market our services to middle market mid-size american businesses. We provide Full Service Payroll (includes the processing of payroll, printing of checks and direct depositing, tax filing, and tax payments), Bookkeeping (Using their native systems, or ours), Contract CFO (with expense reduction analysis), Reporting services for business directors to make informed decisions, Capital Fundraising (Advice on seeking equity to help grow your business), and Taxes (Personal (1040), Partnership (1065), Corporate (1120, 1120S (Including Consolidated Returns)), Trust (1041) and Non-Profit (990)), including all affiliated state returns. One of our major selling points is our variety of experience, and our fast turn around times on projects.
This project specifically, I would like to highlight the bookkeeping services, but still want the tax and payroll services listed on the postcard.
I have uploaded the logo design for BRELLVO and would like a postcard that compliments the logo.
Company contact info is:
Brellvo accounting services Inc
P.O. Box 4638
Great falls, MT 59172
(800) 613-2794
Www.brellvo-example.com
Target Market(s)
Small to medium size businesses
Industry/Entity Type
Accounting
Look and feel

```html
<!DOCTYPE html>
<html lang="en">
<head>
<meta charset="utf-8">
<title>Brellvo Postcard</title>
<link rel="stylesheet" href="https://fonts.googleapis.com/css2?family=Bebas+Neue&family=Montserrat:wght@500;700&family=Tinos:wght@700&display=swap">
<style>
  :root {
    --green: #4fb847;
    --green-text: #3fae3a;
    --yellow: #f5c400;
    --dark: #222222;
    --ink: #1a1a1a;
    --white: #ffffff;
    --page: #eeeeee;
    --rule: #555555;
  }
  * { margin: 0; padding: 0; box-sizing: border-box; }
  html, body { width: 1200px; height: 2230px; overflow: hidden; background: var(--page); }
  .sheet { position: relative; width: 1200px; height: 2230px; }
  .postcard {
    position: absolute; left: 50px; width: 1100px; height: 712px;
    background: var(--white); overflow: hidden;
    box-shadow: 0 6px 18px rgba(0,0,0,0.18);
  }
  .postcard--front { top: 343px; }
  .postcard--back { top: 1175px; }
  .shapes { position: absolute; inset: 0; width: 1100px; height: 712px; }
  .abs { position: absolute; }

  .brand { display: flex; align-items: center; gap: 12px; font-family: "Tinos", serif; font-weight: 700; color: var(--ink); }
  .brand__dot { border-radius: 50%; background: var(--yellow); flex: none; }
  .front-brand { left: 50px; top: 44px; font-size: 48px; }
  .front-brand .brand__dot { width: 40px; height: 40px; }

  .headline { left: 53px; top: 204px; font-family: "Bebas Neue", sans-serif; font-size: 94px; line-height: 88px; color: var(--white); }
  .headline__name { display: block; font-family: "Tinos", serif; font-weight: 700; font-size: 74px; line-height: 92px; color: var(--ink); }
  .book-now {
    left: 53px; top: 497px; width: 205px; height: 46px; border-radius: 23px;
    background: var(--yellow); border: 2px solid #c9a000;
    display: flex; align-items: center; justify-content: center; gap: 14px;
    font-family: "Tinos", serif; font-weight: 700; font-size: 25px; color: var(--ink);
  }
  .schedule { left: 53px; top: 590px; font-family: "Montserrat", sans-serif; font-weight: 700; font-size: 29px; color: var(--green-text); letter-spacing: 0.5px; }
  .front-url { left: 53px; top: 630px; font-family: "Montserrat", sans-serif; font-weight: 500; font-size: 36px; color: var(--ink); }
  .call-label { left: 640px; top: 584px; font-family: "Montserrat", sans-serif; font-weight: 700; font-size: 29px; color: var(--green-text); }
  .call-phone { left: 640px; top: 622px; display: flex; align-items: center; gap: 14px; font-family: "Tinos", serif; font-weight: 700; font-size: 50px; color: var(--white); }

  .service-tab { left: 30px; top: 60px; font-family: "Tinos", serif; font-weight: 700; font-size: 25px; color: var(--white); }
  .service-list { left: 48px; top: 124px; width: 440px; list-style: none; font-family: "Montserrat", sans-serif; font-weight: 500; font-size: 13.5px; line-height: 18px; color: var(--ink); }
  .service-list li { display: flex; gap: 14px; margin-bottom: 16px; }
  .service-list svg { flex: none; margin-top: 2px; }
  .back-contact { left: 42px; font-family: "Montserrat", sans-serif; font-weight: 500; color: var(--white); display: flex; align-items: center; gap: 16px; }
  .back-contact--phone { top: 580px; font-size: 42px; }
  .back-contact--web { top: 642px; font-size: 31px; }

  .back-brand { left: 620px; top: 62px; font-size: 28px; }
  .back-brand .brand__dot { width: 24px; height: 24px; }
  .return-address { left: 620px; top: 134px; display: flex; gap: 8px; font-family: "Montserrat", sans-serif; font-weight: 500; font-size: 13px; line-height: 17px; color: var(--ink); }
  .stamp-box { left: 917px; top: 73px; width: 126px; height: 126px; background: #f2f2f2; border: 1px solid #cccccc; }
  .address-line { left: 621px; width: 422px; height: 2px; background: var(--rule); }
</style>
</head>
<body>
<main class="sheet">

  <section class="postcard postcard--front" aria-label="Postcard front">
    <svg class="shapes" viewBox="0 0 1100 712" aria-hidden="true">
      <defs>
        <linearGradient id="photoTone" x1="0" y1="0" x2="1" y2="1">
          <stop offset="0" stop-color="#d9dde0"/>
          <stop offset="0.5" stop-color="#c7c2b8"/>
          <stop offset="1" stop-color="#a9a49b"/>
        </linearGradient>
      </defs>
      <rect x="480" y="151" width="620" height="420" fill="url(#photoTone)" role="img" aria-label="Photo of a smiling accountant at a desk with a laptop reviewing a chart report"/>
      <polygon points="0,151 512,151 598,571 0,571" fill="var(--green)"/>
      <polygon points="600,571 1100,571 1100,712 552,712" fill="var(--dark)"/>
      <polygon points="586,571 604,571 556,712 538,712" fill="var(--yellow)"/>
    </svg>

    <div class="abs brand front-brand"><span class="brand__dot"></span>BRELLVO</div>

    <h1 class="abs headline">VIRTUAL CPA<br>FIRM CALLED<span class="headline__name">“BRELLVO”</span></h1>

    <div class="abs book-now">Book Now
      <svg width="24" height="24" viewBox="0 0 24 24" aria-hidden="true"><circle cx="12" cy="12" r="12" fill="var(--dark)"/><path d="M10 7l5 5-5 5" stroke="var(--white)" stroke-width="2.6" fill="none"/></svg>
    </div>

    <p class="abs schedule">SCHEDULE ONLLINE</p>
    <p class="abs front-url">www.brellvo-example.com</p>

    <p class="abs call-label">Call us now:</p>
    <p class="abs call-phone">
      <svg width="34" height="34" viewBox="0 0 24 24" aria-hidden="true"><circle cx="12" cy="12" r="12" fill="var(--yellow)"/><path d="M8.2 6.5l2 2.6-1.1 1.4c.8 1.6 2 2.8 3.6 3.6l1.4-1.1 2.6 2-1.2 1.8c-4.2-.4-8.3-4.5-8.7-8.7z" fill="var(--dark)"/></svg>
      (800) 613-2794
    </p>
  </section>

  <section class="postcard postcard--back" aria-label="Postcard back">
    <svg class="shapes" viewBox="0 0 1100 712" aria-hidden="true">
      <polygon points="0,53 350,53 366,73 350,94 0,94" fill="var(--green)"/>
      <polyline points="436,0 550,488 518,565" fill="none" stroke="#dddddd" stroke-width="10"/>
      <polyline points="432,0 546,488 514,565" fill="none" stroke="var(--yellow)" stroke-width="5"/>
      <polygon points="0,565 550,565 550,712 0,712" fill="var(--dark)"/>
    </svg>

    <p class="abs service-tab">We provide Full Service</p>

    <ul class="abs service-list">
      <li><svg width="13" height="13" viewBox="0 0 13 13" aria-hidden="true"><rect x="0.5" y="0.5" width="12" height="12" rx="2" fill="none" stroke="var(--green)"/><path d="M3 6.5l2.4 2.4L10 4" stroke="var(--green)" stroke-width="1.6" fill="none"/></svg><span>Payroll (includes the processing of payroll,<br>Printing of checks and direct depositing,<br>Tax filing,and tax payments),</span></li>
      <li><svg width="13" height="13" viewBox="0 0 13 13" aria-hidden="true"><rect x="0.5" y="0.5" width="12" height="12" rx="2" fill="none" stroke="var(--green)"/><path d="M3 6.5l2.4 2.4L10 4" stroke="var(--green)" stroke-width="1.6" fill="none"/></svg><span>Bookkeeping (Using their native systems, or ours),</span></li>
      <li><svg width="13" height="13" viewBox="0 0 13 13" aria-hidden="true"><rect x="0.5" y="0.5" width="12" height="12" rx="2" fill="none" stroke="var(--green)"/><path d="M3 6.5l2.4 2.4L10 4" stroke="var(--green)" stroke-width="1.6" fill="none"/></svg><span>Contract CFO (with expense reduction analysis),</span></li>
      <li><svg width="13" height="13" viewBox="0 0 13 13" aria-hidden="true"><rect x="0.5" y="0.5" width="12" height="12" rx="2" fill="none" stroke="var(--green)"/><path d="M3 6.5l2.4 2.4L10 4" stroke="var(--green)" stroke-width="1.6" fill="none"/></svg><span>Reporting services for business directors to make<br>informed decisions,</span></li>
      <li><svg width="13" height="13" viewBox="0 0 13 13" aria-hidden="true"><rect x="0.5" y="0.5" width="12" height="12" rx="2" fill="none" stroke="var(--green)"/><path d="M3 6.5l2.4 2.4L10 4" stroke="var(--green)" stroke-width="1.6" fill="none"/></svg><span>Capital Fundraising (Advice on seeking equity<br>to help grow your business),</span></li>
      <li><svg width="13" height="13" viewBox="0 0 13 13" aria-hidden="true"><rect x="0.5" y="0.5" width="12" height="12" rx="2" fill="none" stroke="var(--green)"/><path d="M3 6.5l2.4 2.4L10 4" stroke="var(--green)" stroke-width="1.6" fill="none"/></svg><span>And Taxes (Personal (1040),</span></li>
      <li><svg width="13" height="13" viewBox="0 0 13 13" aria-hidden="true"><rect x="0.5" y="0.5" width="12" height="12" rx="2" fill="none" stroke="var(--green)"/><path d="M3 6.5l2.4 2.4L10 4" stroke="var(--green)" stroke-width="1.6" fill="none"/></svg><span>Partnership (1065),</span></li>
      <li><svg width="13" height="13" viewBox="0 0 13 13" aria-hidden="true"><rect x="0.5" y="0.5" width="12" height="12" rx="2" fill="none" stroke="var(--green)"/><path d="M3 6.5l2.4 2.4L10 4" stroke="var(--green)" stroke-width="1.6" fill="none"/></svg><span>Corporate (1120, 1120S (Including Consolidated Returns)),</span></li>
      <li><svg width="13" height="13" viewBox="0 0 13 13" aria-hidden="true"><rect x="0.5" y="0.5" width="12" height="12" rx="2" fill="none" stroke="var(--green)"/><path d="M3 6.5l2.4 2.4L10 4" stroke="var(--green)" stroke-width="1.6" fill="none"/></svg><span>Trust (1041) and Non-Profit (990)),</span></li>
      <li><svg width="13" height="13" viewBox="0 0 13 13" aria-hidden="true"><rect x="0.5" y="0.5" width="12" height="12" rx="2" fill="none" stroke="var(--green)"/><path d="M3 6.5l2.4 2.4L10 4" stroke="var(--green)" stroke-width="1.6" fill="none"/></svg><span>Including all affiliated state returns</span></li>
    </ul>

    <p class="abs back-contact back-contact--phone">
      <svg width="30" height="30" viewBox="0 0 24 24" aria-hidden="true"><circle cx="12" cy="12" r="12" fill="var(--yellow)"/><path d="M8.2 6.5l2 2.6-1.1 1.4c.8 1.6 2 2.8 3.6 3.6l1.4-1.1 2.6 2-1.2 1.8c-4.2-.4-8.3-4.5-8.7-8.7z" fill="var(--dark)"/></svg>
      (800) 613-2794
    </p>
    <p class="abs back-contact back-contact--web">
      <svg width="30" height="30" viewBox="0 0 24 24" aria-hidden="true"><circle cx="12" cy="12" r="11" fill="var(--yellow)"/><g stroke="var(--dark)" stroke-width="1.3" fill="none"><circle cx="12" cy="12" r="7"/><ellipse cx="12" cy="12" rx="3" ry="7"/><path d="M5 12h14M6 8.5h12M6 15.5h12"/></g></svg>
      www.brellvo-example.com
    </p>

    <div class="abs brand back-brand"><span class="brand__dot"></span>BRELLVO</div>
    <div class="abs return-address">
      <svg width="11" height="15" viewBox="0 0 11 15" aria-hidden="true"><path d="M5.5 0a5.5 5.5 0 0 0-5.5 5.5c0 4 5.5 9.5 5.5 9.5s5.5-5.5 5.5-9.5A5.5 5.5 0 0 0 5.5 0z" fill="var(--green)"/><circle cx="5.5" cy="5.5" r="2" fill="var(--white)"/></svg>
      <p>Brellvo accounting services Inc<br>P.O. Box 4638<br>Great falls, MT 59172</p>
    </div>
    <div class="abs stamp-box" aria-label="Stamp area"></div>
    <div class="abs address-line" style="top:378px"></div>
    <div class="abs address-line" style="top:440px"></div>
    <div class="abs address-line" style="top:506px"></div>
    <div class="abs address-line" style="top:571px"></div>
  </section>

</main>
</body>
</html>
```